Killer business card for bowling event and marketing company

Rolling 'T' Ventures is a sports marketing company that specializes in unique bowling events that provide return on investment for sponsors and memorable experiences for participants and spectators. We need a new business card that simultaneously communicates professionalism and fun. Our preferred colors are black and re

Target Market(s)

Executives in the marketing and sponsorship departments of companies, tourism executives, bowling center owners, and people who love to bowl.

Industry/Entity Type

Business

Contact Information for Business Card

Neil T Farrow
Rolling 'T' Ventures
PO Box 47
Cedar Ridge, Oregon USA 00000
Email: neilt@rollingtventures.example
Mobile: 1-555-318-4762

Requirements
Must have
• Our preferred colors are black and red.
Nice to have
• I am considering the use of the attached image for the back of the card.

```html
<!DOCTYPE html>
<html lang="en">
<head>
<meta charset="utf-8">
<title>Rolling 'T' Ventures – Business Card</title>
<link rel="stylesheet" href="https://fonts.googleapis.com/css2?family=Bebas+Neue&family=Roboto:wght@700&family=Josefin+Sans:wght@300;400&display=swap">
<style>
  :root {
    --backdrop: #e6e6e3;
    --card-white: #f7f7f5;
    --slate: #808184;
    --edge-grey: #a7a9ac;
    --signal-orange: #f15a29;
    --fold-orange: #d9472b;
    --ink: #3a3a3c;
  }
  html, body {
    margin: 0;
    padding: 0;
    width: 1200px;
    height: 825px;
    overflow: hidden;
    background: var(--backdrop);
  }
  .canvas {
    position: relative;
    width: 1200px;
    height: 825px;
  }
  .business-card {
    position: absolute;
    left: 106px;
    top: 108px;
    width: 988px;
    height: 608px;
    display: block;
    box-shadow: 0 10px 28px rgba(0, 0, 0, 0.18);
  }
  .card-bg { fill: var(--card-white); }
  .edge-strip { fill: var(--edge-grey); }
  .slate-panel { fill: var(--slate); }
  .accent-bar { fill: var(--signal-orange); }
  .name-ribbon { fill: var(--signal-orange); }
  .ribbon-fold { fill: var(--fold-orange); }
  .company-name {
    font-family: 'Roboto', Arial, sans-serif;
    font-weight: 700;
    font-size: 28px;
    fill: #ffffff;
  }
  .person-name {
    font-family: 'Bebas Neue', 'Oswald', sans-serif;
    font-size: 42px;
    fill: #ffffff;
    letter-spacing: 0.3px;
  }
  .contact-line {
    font-family: 'Josefin Sans', Arial, sans-serif;
    font-weight: 300;
    font-size: 13.5px;
    fill: var(--ink);
  }
  .contact-icon { fill: var(--signal-orange); }
  .contact-icon-stroke {
    fill: none;
    stroke: var(--signal-orange);
    stroke-width: 1.4;
  }
</style>
</head>
<body>
<main class="canvas">
  <svg class="business-card" viewBox="0 0 706 434" xmlns="http://www.w3.org/2000/svg" aria-label="Rolling 'T' Ventures business card for Neil T Farrow">
    <rect class="card-bg" x="0" y="0" width="706" height="434"/>
    <polygon class="slate-panel" points="0,0 501,0 321,434 0,434"/>
    <rect class="edge-strip" x="0" y="0" width="13" height="434"/>
    <rect class="accent-bar" x="13" y="0" width="20" height="434"/>

    <text class="company-name" x="50" y="227">Rolling 'T' Ventures</text>

    <polygon class="ribbon-fold" points="365,163 433,163 413,213"/>
    <rect class="name-ribbon" x="365" y="103" width="341" height="60"/>
    <text class="person-name" x="689" y="148" text-anchor="end">Neil T Farrow</text>

    <g class="contact-block">
      <text class="contact-line" x="673" y="356" text-anchor="end">1-555-318-4762</text>
      <path class="contact-icon-stroke" d="M682,346 q-2,5 1,9 q2,2 5,1"/>

      <text class="contact-line" x="673" y="378" text-anchor="end">neilt@rollingtventures.example</text>
      <rect class="contact-icon" x="681" y="370" width="9" height="6"/>

      <text class="contact-line" x="673" y="400" text-anchor="end">PO Box 47 Cedar Ridge, Oregon USA 00000</text>
      <path class="contact-icon-stroke" d="M685.5,399 l-2.6,-4.2 a3,3 0 1 1 5.2,0 z"/>
    </g>
  </svg>
</main>
</body>
</html>
```